Business Card Design

We are a flooring/granite/cabinet company
want a sleek and modern design card. Will send our logo. maybe our logo in 3d on card.
black card

Industry/Entity Type

Business

Contact Information for Business Card

Daniel Restrepo
company name Stonecrest Tile Depot
4728 loop 60w 78419
210-647-3928
stonecresttiledepot@mailbarn.net

```html
<!DOCTYPE html>
<html lang="en">
<head>
<meta charset="UTF-8">
<title>Stonecrest Tile Depot — Business Card</title>
<link href="https://fonts.googleapis.com/css2?family=Michroma&family=Roboto:wght@400&display=swap" rel="stylesheet">
<style>
  :root {
    --page-bg: #ffffff;
    --card-black: #0d0e10;
    --card-black-light: #1c1e22;
    --card-back: #141414;
    --brand-blue: #0b4565;
    --brand-blue-bright: #13587f;
    --silver: #b9bcc0;
    --text-grey: #9a9ea3;
  }
  * { box-sizing: border-box; margin: 0; padding: 0; }
  html, body {
    width: 1200px;
    height: 800px;
    overflow: hidden;
    background: var(--page-bg);
  }
  .canvas {
    position: relative;
    width: 1200px;
    height: 800px;
  }
  .card {
    position: absolute;
    top: 245px;
    width: 540px;
    height: 309px;
    border-radius: 22px;
    overflow: hidden;
    box-shadow: 0 6px 18px rgba(0, 0, 0, 0.28);
  }
  .card-front {
    left: 40px;
    background: linear-gradient(160deg, var(--card-black-light) 0%, var(--card-black) 70%);
  }
  .card-back {
    left: 620px;
    background: var(--card-back);
    display: flex;
    align-items: center;
    justify-content: center;
  }
  .corner-bands {
    position: absolute;
    inset: 0;
    width: 100%;
    height: 100%;
  }
  .front-content {
    position: absolute;
    left: 122px;
    top: 60px;
  }
  .brand-name {
    font-family: "Michroma", sans-serif;
    color: var(--brand-blue-bright);
    display: flex;
    align-items: center;
    gap: 8px;
    white-space: nowrap;
  }
  .brand-mark {
    width: 10px;
    height: 10px;
    background: var(--brand-blue-bright);
  }
  .front-content .brand-name {
    font-size: 12px;
    letter-spacing: 1px;
    margin-bottom: 26px;
  }
  .person-name {
    font-family: "Michroma", sans-serif;
    font-size: 20px;
    font-weight: 400;
    letter-spacing: 1.5px;
    color: var(--brand-blue-bright);
    text-transform: uppercase;
    margin-bottom: 14px;
    white-space: nowrap;
  }
  .contact-list {
    list-style: none;
    font-family: "Roboto", Arial, sans-serif;
    font-size: 15px;
    color: var(--text-grey);
  }
  .contact-list li {
    display: flex;
    align-items: center;
    gap: 9px;
    margin-bottom: 8px;
  }
  .contact-icon {
    width: 12px;
    height: 12px;
    flex: none;
  }
  .card-back .brand-name {
    font-size: 27px;
    letter-spacing: 2px;
    gap: 14px;
  }
  .card-back .brand-mark {
    width: 18px;
    height: 18px;
  }
</style>
</head>
<body>
<main class="canvas">
  <section class="card card-front" aria-label="Business card front">
    <svg class="corner-bands" viewBox="0 0 540 309" preserveAspectRatio="none" aria-hidden="true">
      <polygon points="0,0 112,0 38,309 0,309" fill="var(--brand-blue)"/>
      <line x1="112" y1="0" x2="38" y2="309" stroke="var(--silver)" stroke-width="3"/>
      <polygon points="540,0 502,0 428,309 540,309" fill="var(--brand-blue)"/>
      <line x1="502" y1="0" x2="428" y2="309" stroke="var(--silver)" stroke-width="3"/>
    </svg>
    <div class="front-content">
      <div class="brand-name"><span class="brand-mark"></span>Stonecrest Tile Depot</div>
      <h1 class="person-name">Daniel Restrepo</h1>
      <ul class="contact-list">
        <li>
          <svg class="contact-icon" viewBox="0 0 12 12" aria-hidden="true">
            <rect width="12" height="12" rx="2" fill="var(--brand-blue-bright)"/>
            <path d="M3.6 2.8l1.3 1.4-.7 1c.5 1 1.2 1.7 2.2 2.2l1-.7 1.4 1.3-.8 1.2C5.6 8.9 3.1 6.4 2.8 3.6z" fill="#0d0e10"/>
          </svg>
          210-647-3928
        </li>
        <li>
          <svg class="contact-icon" viewBox="0 0 12 12" aria-hidden="true">
            <rect width="12" height="12" rx="2" fill="var(--brand-blue-bright)"/>
            <rect x="2.5" y="3.5" width="7" height="5" fill="none" stroke="#0d0e10" stroke-width="1"/>
            <path d="M2.5 3.5L6 6.3 9.5 3.5" fill="none" stroke="#0d0e10" stroke-width="1"/>
          </svg>
          stonecresttiledepot@mailbarn.net
        </li>
      </ul>
    </div>
  </section>

  <section class="card card-back" aria-label="Business card back">
    <div class="brand-name"><span class="brand-mark"></span>Stonecrest Tile Depot</div>
  </section>
</main>
</body>
</html>
```